High End Notary Service Business Card Design

Want a professional and elegant/luxurious business card that is clean and simple in the design. A notary is a trusted professional that helps people sign very important documents. The card should be in alignment with this service provided.

Most of the time, service will be for the purchase of a home or refinance of a mortgage

There is NO LOGO. This is aesthetic. A look and feel. Conveying professionalism and concierge level of service.

Target Market(s)

Other business professionals, Lawyers, Escrow Officers, Loan Officers

Industry/Entity Type

Legal

Contact Information for Business Card

This will be a one-sided business card

Colors
35a7d7
3176b5
85cae6
d3a5cc
b868aa
ffffff
0356a4

Requirements
Must have
• Lorena T. Mirabel-Hodgkins
Notary Public

642-871-3094
MirabelSigningDesk@Wexmail.com
Nice to have
• Headshot photo below. Convey the aspect of signing documents. No black cards. Preference is shades of blue: light blue, navy, aqua, gold, white, or lavendar, etc.
Should not have
• No scales or legal scales.

```html
<!DOCTYPE html>
<html lang="en">
<head>
<meta charset="utf-8">
<title>Notary Public – Lorena T. Mirabel-Hodgkins</title>
<link rel="stylesheet" href="https://fonts.googleapis.com/css2?family=EB+Garamond:wght@400&family=Pinyon+Script&display=swap">
<style>
  :root {
    --sky: #35a7d7;
    --ocean: #3176b5;
    --ink: #161616;
    --white: #ffffff;
    --paper-light: #e9e6e2;
    --paper-mid: #c9c4bf;
    --wood: #8a7f78;
  }
  * { margin: 0; padding: 0; box-sizing: border-box; }
  html, body {
    width: 1200px;
    height: 788px;
    overflow: hidden;
    background: var(--white);
  }
  .card {
    position: relative;
    width: 1200px;
    height: 788px;
    overflow: hidden;
  }
  .card-art {
    position: absolute;
    inset: 0;
    width: 1200px;
    height: 788px;
  }
  .title {
    position: absolute;
    left: 52px;
    top: 215px;
    font-family: "Pinyon Script", cursive;
    font-size: 96px;
    line-height: 1;
    color: var(--ink);
    white-space: nowrap;
  }
  .contact {
    position: absolute;
    font-family: "EB Garamond", serif;
    color: var(--white);
    white-space: nowrap;
    line-height: 1;
  }
  .contact-name { left: 604px; top: 476px; font-size: 48px; }
  .contact-phone { left: 617px; top: 642px; font-size: 29px; }
  .contact-email { left: 609px; top: 718px; font-size: 29px; }
</style>
</head>
<body>
  <main class="card">
    <svg class="card-art" viewBox="0 0 1200 788" xmlns="http://www.w3.org/2000/svg">
      <defs>
        <linearGradient id="desk-tones" x1="0" y1="0" x2="1" y2="1">
          <stop offset="0" stop-color="var(--paper-mid)"/>
          <stop offset="0.35" stop-color="var(--paper-light)"/>
          <stop offset="0.7" stop-color="var(--paper-light)"/>
          <stop offset="1" stop-color="var(--wood)"/>
        </linearGradient>
      </defs>
      <rect class="signing-scene" role="img" aria-label="Photo of a fountain pen resting on sheets of paper on a wooden desk" x="0" y="0" width="1200" height="788" fill="url(#desk-tones)"/>
      <path class="wave-fill" d="M0,700 C240,650 440,430 640,372 C860,310 1010,150 1200,72 L1200,788 L0,788 Z" fill="var(--sky)"/>
      <path class="wave-edge" d="M0,700 C240,650 440,430 640,372 C860,310 1010,150 1200,72" fill="none" stroke="var(--ocean)" stroke-width="16"/>
      <g class="rule-lines" stroke="var(--white)" stroke-width="3">
        <line x1="120" y1="625" x2="1200" y2="625"/>
        <line x1="0" y1="700" x2="1200" y2="700"/>
        <line x1="1040" y1="116" x2="1200" y2="116"/>
      </g>
    </svg>

    <h1 class="title">Notary Public</h1>
    <p class="contact contact-name">Lorena T. Mirabel-Hodgkins</p>
    <p class="contact contact-phone">642-871-3094</p>
    <p class="contact contact-email">MirabelSigningDesk@Wexmail.com</p>
  </main>
</body>
</html>
```